Cobalt Field Services website design

We want to create a Sports turf website for our business Cobalt Field Services - we do sports turf management on sports fields around the Brackenridge region soccer rugby league softball fields etc from full turf management plans and maintenance to just supply and apply of turf management products and just supply of products with program we also do grounds facility maintenance at council facility's and grounds that require a higher level of care - we will up load our logos and fonts etc to assist with the colour pallet for the website - we will have to have a landing page a shop page with tabs a gallery tab along with a grants initiative and our northreach finest green tab also - our font for the txt is called ethnocentric
Updates

how do we open time for people to submit we have no one submitted

Industry/Entity Type

Turf

Coding

Coded - Design and coding required

Number of Pages Required

5+ page

Font styles to use
Other font styles liked:
• ethnocentric

Requirements
Must have
• I have mentioned some waffle in the description that should assist
Should not have
• anything not related

```html
<!DOCTYPE html>
<html lang="en">
<head>
<meta charset="utf-8">
<title>Cobalt Field Services — Sports Turf Specialists</title>
<link rel="stylesheet" href="https://fonts.googleapis.com/css2?family=Orbitron:wght@800&family=Montserrat:wght@400;500;600;700&display=swap">
<style>
:root{
  --green:#0f7a1c;
  --green-dark:#0a5a14;
  --lime:#7bc62d;
  --blue:#0aa3e8;
  --pale-blue:#e6f4fb;
  --ink:#1d1d1d;
  --muted:#4a4a4a;
  --white:#ffffff;
  --black:#000000;
  --head:"Orbitron",sans-serif;
  --body:"Montserrat",sans-serif;
}
*{box-sizing:border-box;margin:0;padding:0}
html,body{width:1200px;height:4898px;overflow:hidden}
body{position:relative;background:var(--white);font-family:var(--body);color:var(--ink)}
.abs{position:absolute}
h1,h2,h3,.logo-name,.product-label,.eyebrow,.footer-name{font-family:var(--head);text-transform:uppercase;font-weight:800;letter-spacing:1.5px}
.btn{display:inline-block;font-family:var(--body);font-weight:600;font-size:10px;text-transform:uppercase;border-radius:20px;padding:9px 20px;color:var(--white);text-decoration:none}
.btn-green{background:var(--green)}
.btn-blue{background:var(--blue)}
.btn-lime{background:var(--lime)}
.btn-ghost{border:1.5px solid var(--white);background:transparent}

/* header */
.site-header{top:0;left:0;width:1200px;height:62px;background:var(--white);display:flex;align-items:center;justify-content:space-between;padding:0 90px 0 95px}
.logo-name{font-size:16px;color:var(--green)}
.main-nav{display:flex;align-items:center;gap:24px;font-size:10px;font-weight:600;text-transform:uppercase;color:var(--ink)}
.main-nav .home{width:10px;height:10px;display:block}

/* hero */
.hero{top:62px;left:0;width:1200px;height:723px;background:linear-gradient(160deg,#1d3510 0%,#4f7d1d 35%,#a6b62a 60%,#3f6a15 100%)}
.hero-copy{left:95px;top:334px;color:var(--white)}
.hero-copy h1{font-size:32px;line-height:44px;margin-bottom:12px}
.hero-copy p{font-size:11.5px;line-height:19px;font-weight:500;margin-bottom:16px}
.hero-copy .btn{margin-right:4px}
.slide-arrow{width:26px;height:60px;background:rgba(0,0,0,.35);color:#fff;font-size:12px;display:flex;align-items:center;justify-content:center}
.scroll-cue{left:590px;top:708px;width:18px;height:28px;border:2px solid #fff;border-radius:10px}

/* about */
.about-stripes{left:135px;top:785px;width:425px;height:430px;background:linear-gradient(90deg,#2f8a2b,#67b83c 40%,#3d9b32 70%,#8cc4e6);clip-path:path("M0 0 H425 V300 A130 130 0 0 1 295 430 H130 A130 130 0 0 1 0 300 Z")}
.eyebrow{font-size:13px;color:var(--green)}
.about-copy{left:618px;top:943px;width:480px}
.about-copy h2{font-size:25px;line-height:37px;margin:6px 0 12px}
.about-copy p{font-size:11px;line-height:17px;color:var(--muted);margin-bottom:10px}
.about-copy ul{list-style:none;font-size:11px;line-height:19px;color:var(--muted)}
.about-copy li::before{content:"";display:inline-block;width:8px;height:8px;border-radius:50%;background:var(--green);margin-right:7px}

/* section titles */
.section-title{left:0;width:1200px;text-align:center}
.section-title h2{font-size:28px;margin-bottom:10px}
.section-title p{font-size:11px;color:var(--muted)}

/* cards */
.card-img{border-radius:14px}
.card-label h3{font-size:12.5px;line-height:16px;margin-bottom:6px}
.card-label p{font-size:10.5px;line-height:14px;color:var(--muted)}

/* work banner */
.work-banner{left:0;top:2004px;width:1200px;height:499px;background:linear-gradient(180deg,#8fbad6 0%,#e6e2c9 40%,#5f9a2e 62%,#2f6a18 100%)}
.work-banner h3{left:92px;top:356px;font-size:29px;line-height:33px;color:var(--white)}

/* features */
.feature h3{font-size:14px;line-height:18px;margin-bottom:12px}
.feature p{font-size:10.5px;line-height:15px;color:var(--muted);margin-bottom:10px}
.feature a{font-size:10.5px;color:var(--green);text-decoration:none;font-weight:500}

.product-label{text-align:center;font-size:12.5px;line-height:16px}

/* testimonial */
.quote-mark{left:212px;top:3722px;font-family:Georgia,serif;font-size:110px;line-height:80px;color:var(--green);font-weight:700}
.testimonial{left:215px;top:3785px;width:420px}
.testimonial h2{font-size:29px;line-height:38px;margin-bottom:14px}
.testimonial p{font-size:15px;line-height:23px;color:var(--muted);margin-bottom:14px}
.testimonial .client{font-weight:700;font-size:14px;margin-bottom:16px}
.dots{display:flex;gap:6px}
.dots span{width:32px;height:32px;border-radius:50%;background:var(--green);color:#fff;display:flex;align-items:center;justify-content:center;font-size:13px}
.dots span + span{background:var(--blue)}
.client-visual{left:650px;top:3620px;width:360px;height:460px;border-radius:16px;background:var(--pale-blue)}

/* contact CTA */
.cta-stripes{left:160px;top:4105px;width:380px;height:420px;background:linear-gradient(180deg,#9cc8ea 0%,#cde5f2 35%,#4c9a2e 60%,#2d6a1a 100%);clip-path:path("M0 0 H380 V290 A130 130 0 0 1 250 420 H130 A130 130 0 0 1 0 290 Z")}
.cta-copy{left:608px;top:4190px;width:470px}
.cta-copy h2{font-size:28px;line-height:38px;margin-bottom:14px}
.cta-copy p{font-size:11px;line-height:18px;color:var(--muted);margin-bottom:12px}
.cta-copy ul{list-style:none;font-size:11px;line-height:22px;color:var(--ink);margin-bottom:16px}
.cta-copy svg{width:11px;height:11px;vertical-align:-1px;margin-right:8px}

/* footer */
.site-footer{left:0;top:4540px;width:1200px;height:358px;background:var(--black);color:var(--white);text-align:center}
.footer-name{position:absolute;left:0;top:100px;width:1200px;font-size:26px;color:var(--white)}
.footer-nav{position:absolute;left:0;top:170px;width:1200px;display:flex;justify-content:center;gap:22px;font-size:11px;font-weight:500}
.socials{position:absolute;left:0;top:206px;width:1200px;display:flex;justify-content:center;gap:8px}
.socials span{width:34px;height:34px;border-radius:50%;background:var(--blue)}
.socials span:nth-child(3){background:#b5329c}
.socials span:nth-child(4){background:#2a4f9a}
.footer-legal{position:absolute;left:0;top:300px;width:1200px;font-size:10.5px;line-height:17px}
.to-top{position:absolute;right:25px;top:56px;width:34px;height:34px;border-radius:50%;background:var(--lime);color:#fff;font-size:14px;display:flex;align-items:center;justify-content:center}
</style>
</head>
<body>

<header class="site-header abs">
  <div class="logo-name">Cobalt Field Services</div>
  <nav class="main-nav">
    <svg class="home" viewBox="0 0 10 10"><path d="M5 0 L10 5 H8.5 V10 H1.5 V5 H0 Z" fill="#0aa3e8"/></svg>
    <span>Shop</span><span>Gallery</span><span>Grants Initiative</span><span>Northreach Finest Green</span><span>Contact</span>
    <a class="btn btn-green">Get a Turf Quote</a>
  </nav>
</header>

<section class="hero abs" role="img" aria-label="Aerial view of a sports field at sunset with striped mown grass"></section>
<div class="slide-arrow abs" style="left:0;top:388px">‹</div>
<div class="slide-arrow abs" style="left:1174px;top:388px">›</div>
<div class="hero-copy abs">
  <h1>Brackenridge's Sports<br>Turf Specialists</h1>
  <p>From full turf management plans to complete field maintenance —<br>we keep your grounds game-ready, all year round.</p>
  <a class="btn btn-blue">Request a Free Quote</a>
  <a class="btn btn-ghost">View Our Work</a>
</div>
<div class="scroll-cue abs"></div>

<div class="about-stripes abs" role="img" aria-label="Collage of vertical strips showing turf, a golf ball and a mower"></div>
<div class="about-copy abs">
  <div class="eyebrow">Professional</div>
  <h2>Turf Management<br>Across Brackenridge</h2>
  <p>At Cobalt Field Services, we take pride in delivering high-quality turf care and maintenance services for sports fields, council grounds, and premium facilities across the Brackenridge region.</p>
  <p>Whether you need a complete turf management plan, supply and apply of turf products, or ongoing maintenance programs, we've got you covered.</p>
  <ul>
    <li>Sports Turf Maintenance</li>
    <li>Turf Management Programs</li>
    <li>Grounds Facility Care</li>
    <li>Product Supply &amp; Application</li>
  </ul>
</div>

<div class="section-title abs" style="top:1318px">
  <h2>Our Expertise</h2>
  <p>Comprehensive turf management and maintenance services tailored to your facility's needs.</p>
</div>

<div class="card-img abs" style="left:140px;top:1406px;width:225px;height:266px;background:linear-gradient(160deg,#4f9a35,#2f7a22)" role="img" aria-label="Aerial view of a marked soccer field"></div>
<div class="card-img abs" style="left:372px;top:1406px;width:225px;height:266px;background:linear-gradient(180deg,#cfd9c8,#6c9a48 55%,#3d7020)" role="img" aria-label="Tractor spraying a field"></div>
<div class="card-img abs" style="left:603px;top:1406px;width:225px;height:266px;background:linear-gradient(160deg,#8ccf45,#4d9b25)" role="img" aria-label="Rake on fresh green grass"></div>
<div class="card-img abs" style="left:835px;top:1406px;width:225px;height:266px;background:linear-gradient(160deg,#2d5a20,#6b8f3a 50%,#34622a)" role="img" aria-label="Aerial view of a sports facility"></div>

<div class="card-label abs" style="left:143px;top:1686px;width:220px"><h3>Turf Management<br>Plans</h3><p>Custom programs for soccer, rugby league, softball, and other sports fields.</p></div>
<div class="card-label abs" style="left:378px;top:1686px;width:220px"><h3>Maintenance &amp;<br>Field Care</h3><p>Mowing, aeration, fertilisation, irrigation checks, and turf health monitoring.</p></div>
<div class="card-label abs" style="left:609px;top:1686px;width:220px"><h3>Supply &amp;<br>Apply</h3><p>Full range of turf care products supplied and professionally applied.</p></div>
<div class="card-label abs" style="left:836px;top:1686px;width:220px"><h3>Facility<br>Maintenance</h3><p>Council and community grounds maintained to professional sports standards.</p></div>

<a class="btn btn-blue abs" style="left:510px;top:1802px">Talk to Our Turf Experts</a>

<div class="section-title abs" style="top:1916px">
  <h2>Our Work in Action</h2>
  <p>See the results of our professional turf care across Brackenridge's top sports facilities.</p>
</div>

<div class="work-banner abs" role="img" aria-label="Stadium field with goal posts under a bright sky">
  <h3 class="abs">Soccer Field<br>Transformation<br>Before &amp; After</h3>
</div>
<div class="slide-arrow abs" style="left:0;top:2224px">‹</div>
<div class="slide-arrow abs" style="left:1174px;top:2224px">›</div>

<a class="btn btn-green abs" style="left:528px;top:2525px">View Full Gallery</a>

<div class="abs" style="left:135px;top:2626px;width:460px;height:286px;background:linear-gradient(180deg,#d9e3d0,#7fae55 50%,#4d8a2c)" role="img" aria-label="Player running through agility ladder drills on a field"></div>
<div class="abs" style="left:605px;top:2626px;width:458px;height:286px;background:linear-gradient(180deg,#3c6a24,#8bb84a 55%,#5e9b2e)" role="img" aria-label="Manicured lawn with garden beds"></div>

<div class="feature abs" style="left:135px;top:2936px;width:450px">
  <h3>Supporting Local Sports<br>Through Grants</h3>
  <p>We're proud to help local clubs and facilities access grants and funding opportunities for turf upgrades and maintenance programs. Learn how we can help you prepare your field for the next season.</p>
  <a>Explore Our Grants Initiative »</a>
</div>
<div class="feature abs" style="left:607px;top:2936px;width:450px">
  <h3>Celebrating Brackenridge's<br>Best Lawns</h3>
  <p>Our community-driven program that rewards the region's most beautiful and well-kept lawns. Whether you're a proud homeowner or a local club, enter your lawn for a chance to be featured!</p>
  <a>Enter the Competition »</a>
</div>

<div class="section-title abs" style="top:3144px">
  <h2>Shop Turf Care Products</h2>
  <p>Explore our range of professional turf care solutions used by Brackenridge's top facilities.</p>
</div>

<div class="card-img abs" style="left:140px;top:3225px;width:225px;height:266px;background:linear-gradient(180deg,#4e8a33,#1f8a3a)" role="img" aria-label="Bag of turf fertiliser on a field"></div>
<div class="card-img abs" style="left:372px;top:3225px;width:225px;height:266px;background:linear-gradient(180deg,#7ea158,#e8ecea 55%,#6aa03a)" role="img" aria-label="Container of wetting agent"></div>
<div class="card-img abs" style="left:603px;top:3225px;width:225px;height:266px;background:linear-gradient(180deg,#b9d4e6,#eef2f5 50%,#7bab4a)" role="img" aria-label="Container of turf growth regulator"></div>
<div class="card-img abs" style="left:835px;top:3225px;width:225px;height:266px;background:linear-gradient(180deg,#6aa33a,#3f8a27)" role="img" aria-label="Worker spraying weeds with a backpack sprayer"></div>

<div class="product-label abs" style="left:140px;top:3512px;width:225px">Turf Fertiliser<br>Packs</div>
<div class="product-label abs" style="left:372px;top:3512px;width:225px">Wetting<br>Agents</div>
<div class="product-label abs" style="left:603px;top:3512px;width:225px">Turf Growth<br>Regulators</div>
<div class="product-label abs" style="left:835px;top:3512px;width:225px">Weed &amp; Pest<br>Control</div>

<a class="btn btn-lime abs" style="left:545px;top:3570px">Visit Shop</a>

<div class="quote-mark abs">“</div>
<div class="testimonial abs">
  <h2>What Our<br>Clients Say</h2>
  <p>Our soccer field has never looked this good — the Cobalt Field team really know their stuff.</p>
  <div class="client">Brackenridge Soccer Club</div>
  <div class="dots"><span>‹</span><span>›</span></div>
</div>
<div class="client-visual abs" role="img" aria-label="Decorative graphic with portraits of happy clients"></div>

<div class="cta-stripes abs" role="img" aria-label="Vertical strips of a green sports field under blue sky"></div>
<div class="cta-copy abs">
  <h2>Let's Keep Your<br>Turf in Top Shape</h2>
  <p>Ready to elevate your field? Whether you need a turf plan, maintenance schedule, or product advice — we're here to help.</p>
  <ul>
    <li><svg viewBox="0 0 10 12"><path d="M5 0a4 4 0 0 1 4 4c0 3-4 8-4 8S1 7 1 4a4 4 0 0 1 4-4z" fill="#0f7a1c"/></svg>Brackenridge Region, QLD</li>
    <li><svg viewBox="0 0 12 12"><path d="M2 1h3l1 3-2 1a7 7 0 0 0 3 3l1-2 3 1v3c-6 0-9-3-9-9z" fill="#0f7a1c"/></svg>+61 7 5550 0192</li>
    <li><svg viewBox="0 0 12 10"><rect x="0" y="1" width="12" height="8" rx="1" fill="#0f7a1c"/><path d="M0 2l6 4 6-4" stroke="#fff" fill="none"/></svg>hello@cobaltfield.example</li>
  </ul>
  <a class="btn btn-green">Request a Free Quote</a>
</div>

<footer class="site-footer abs">
  <div class="footer-name">Cobalt Field Services</div>
  <nav class="footer-nav"><span>Home</span><span>Shop</span><span>Gallery</span><span>Grants Initiative</span><span>Northreach Finest Green</span><span>Contact</span></nav>
  <div class="socials"><span></span><span></span><span></span><span></span></div>
  <div class="footer-legal">Cobalt Field Services © 2025 – All Rights Reserved<br>Proudly maintaining Brackenridge's premier sports fields and facilities.</div>
  <div class="to-top">↑</div>
</footer>

</body>
</html>
```